Premium men's gut health supplement needs a bottle label designed

We’re mossleaf - a premium men’s wellness brand focused on gut health. Our first product is a high-quality daily supplement designed to support digestion, regularity, and internal cleanliness. Backed by science and tailored for modern lifestyles, mossleaf is crafted in the UK and proudly LGBT-owned. It aims to resolve intimacy problems that gay men may experience due to poor digestion but also does not exclude any other orientation - other men may use it simply to improve their digestion.

mossleaf is for health-conscious men who value science-backed supplements and want to feel confident from the inside out. Many of our early adopters will be gay and bisexual men who prioritise gut health as part of their self-care, sexual, and hygiene routine, though the product is equally effective and appealing to anyone seeking premium digestive support.

The product is premium the target customer is male, not specific to one location but primary markets will be US, UK and EU.

I’d like a supplement bottle designed for mossleaf, our premium men’s gut health brand. The focus should be clean, slightly clinical, and minimal - inspired by brands like Varnō and Brek. The key element is the wordmark (mossleaf) on the front, with no additional logo or icon. Lowercase text and a strong, contemporary font are preferred.

The bottle should be aesthetically pleasing so that people are proud to display it on their shelf, instead of hiding it in a cupboard (like Varnō, brek, Ada Penrith, Olvanne etc)

Avoid anything that shows the product as being for LGBT, e.g., no rainbows, men holding hands etc.

The design should be premium, minimalist and not be busy or overwhelming.

I have uploaded a file called "Bottle" to give an idea of the type of container, but please ignore the colours and change as you see fit. This is just for reference for the type of bottle we'll use - all colours are customisable.

I have also uploaded some images for "style" reference, e.g., brek, varno, ada penrith, etc for inspiration.

```html
<!DOCTYPE html>
<html lang="en">
<head>
<meta charset="utf-8">
<title>mossleaf — digestive support label</title>
<link rel="stylesheet" href="https://fonts.googleapis.com/css2?family=Montserrat:wght@300;400;600;700&display=swap">
<style>
  :root {
    --backdrop: #ffffff;
    --label: #262626;
    --ink: #f2f2f2;
    --ink-soft: #d9d9d9;
    --icon-tone: #8a8a8a;
  }
  html, body {
    margin: 0;
    padding: 0;
    width: 1200px;
    height: 1200px;
    overflow: hidden;
    background: var(--backdrop);
  }
  .canvas {
    width: 1200px;
    height: 1200px;
    display: flex;
    align-items: center;
    justify-content: center;
  }
  .label {
    position: relative;
    width: 560px;
    height: 672px;
    background: var(--label);
    color: var(--ink);
    font-family: "Montserrat", sans-serif;
  }
  .wordmark {
    position: absolute;
    top: 62px;
    left: 0;
    right: 0;
    margin: 0;
    text-align: center;
    font-weight: 700;
    font-size: 72px;
    letter-spacing: -1px;
    line-height: 1;
    color: var(--ink);
  }
  .product-name {
    position: absolute;
    top: 236px;
    left: 0;
    right: 0;
    margin: 0;
    text-align: center;
    font-size: 46px;
    line-height: 44px;
    color: var(--ink);
  }
  .product-name .primary { display: block; font-weight: 600; }
  .product-name .secondary { display: block; font-weight: 300; }
  .benefit-tag {
    position: absolute;
    top: 420px;
    left: 158px;
    width: 240px;
    height: 72px;
    box-sizing: border-box;
    border: 1.5px solid var(--ink-soft);
    display: flex;
    align-items: center;
    padding: 0 8px;
    gap: 8px;
  }
  .benefit-tag .tag-icon {
    width: 32px;
    height: 50px;
    background: var(--icon-tone);
    border-radius: 14px 6px 16px 8px;
    opacity: 0.5;
    flex: none;
  }
  .benefit-tag .tag-text {
    font-weight: 300;
    font-size: 26px;
    line-height: 30px;
    color: var(--ink);
    text-align: center;
    flex: 1;
  }
  .net-weight {
    position: absolute;
    top: 596px;
    left: 0;
    right: 0;
    margin: 0;
    text-align: center;
    font-weight: 400;
    font-size: 20px;
    color: var(--ink-soft);
  }
</style>
</head>
<body>
  <main class="canvas">
    <section class="label">
      <h1 class="wordmark">mossleaf</h1>
      <p class="product-name">
        <span class="primary">digestive</span>
        <span class="secondary">support</span>
      </p>
      <div class="benefit-tag">
        <div class="tag-icon" role="img" aria-label="Small line icon of a stomach"></div>
        <div class="tag-text">internal<br>cleanliness</div>
      </div>
      <p class="net-weight">Net Weight: 60 Capsules</p>
    </section>
  </main>
</body>
</html>
```